New banner graphics for Velkora.com website

I've developed a software tool that helps businesses ensure they are working on their most valuable and important work.

I would like a banner graphic for my home page (www.velkora.com) that can somehow capture the value of focus and intentional outcomes.

I had an initial thought of a starry sky that shifts focus to a few bright stars, but while that might sound ok, I think my idea is lame hence I'm coming to you guys.

My sites two primary colors are a soft purple and gray.
#919EC1(purple)
#9E9E9E (gray)

Target Market(s)

B2B for enterprises. Typical customers are CFOs, CIOs/Heads of IT

Industry/Entity Type

Business Software

Number of Pages Required

1 page

Font styles to use
Sans Serif

Colors
b8a6cd
cedeed

Requirements
Must have
• I use Divi as my Wordpress theme and the current main landing page can be seen at www.velkora.com.
• My logo colors are:
• #919EC1(purple)
• #9E9E9E (gray)
Should not have
• Lots of distraction or visual "noise". I want to re-enforce the message that my software is focused on their business and not my products or website.

```html
<!DOCTYPE html>
<html lang="en">
<head>
<meta charset="utf-8">
<title>Is Your Business Strategy</title>
<link rel="stylesheet" href="https://fonts.googleapis.com/css2?family=Raleway:ital,wght@0,200;0,400;1,400&display=swap">
<style>
  :root {
    --ink-light: #ffffff;
    --ink-muted: #c9c9c9;
    --bg-deep: #050505;
    --bg-mid: #2a2a2a;
    --bg-glow: #8a8a8a;
  }
  html, body {
    margin: 0;
    padding: 0;
    width: 1200px;
    height: 675px;
    overflow: hidden;
    background: var(--bg-deep);
  }
  .banner {
    position: relative;
    width: 1200px;
    height: 675px;
    overflow: hidden;
    font-family: "Raleway", Arial, sans-serif;
    color: var(--ink-light);
  }
  .banner-photo {
    position: absolute;
    inset: 0;
    background:
      radial-gradient(ellipse 140px 330px at 700px 430px, var(--bg-glow) 0%, rgba(138,138,138,0.35) 45%, rgba(0,0,0,0) 100%),
      linear-gradient(180deg, var(--bg-deep) 0%, #111 45%, var(--bg-mid) 80%, #1a1a1a 100%);
  }
  .headline {
    position: absolute;
    left: 0;
    width: 1410px;
    top: 82px;
    margin: 0;
    text-align: center;
    font-weight: 200;
    font-size: 46px;
    letter-spacing: 0.5px;
  }
  .choice {
    position: absolute;
    margin: 0;
    font-size: 25px;
    line-height: 33px;
    text-transform: uppercase;
    white-space: nowrap;
  }
  .choice--strong {
    right: 596px;
    text-align: right;
    font-weight: 400;
  }
  .choice--weak {
    font-style: italic;
    font-weight: 400;
  }
  .divider-word {
    position: absolute;
    left: 701px;
    top: 430px;
    transform: translate(-50%, -50%);
    font-size: 22px;
    color: var(--ink-muted);
    margin: 0;
  }
</style>
</head>
<body>
  <main class="banner">
    <div class="banner-photo" role="img" aria-label="Dark chessboard with black chess pieces, a single white king standing in focus at the centre"></div>

    <h1 class="headline">Is Your Business Strategy</h1>

    <p class="choice choice--strong" style="top:291px">Written down</p>
    <p class="choice choice--strong" style="top:388px">Driving projects</p>
    <p class="choice choice--strong" style="top:495px">Shared with the team</p>
    <p class="choice choice--strong" style="top:584px">Measurable</p>

    <p class="divider-word">OR</p>

    <p class="choice choice--weak" style="left:794px; top:291px">Loose thoughts – on the<br>best of days</p>
    <p class="choice choice--weak" style="left:796px; top:388px">Just a set of slides<br>tacked to walls</p>
    <p class="choice choice--weak" style="left:804px; top:495px">Kept top secret<br>just to be safe</p>
    <p class="choice choice--weak" style="left:832px; top:584px">More art than science</p>
  </main>
</body>
</html>
```